Brightwell Pictures Business Card

Hello,

i would like to have a dynamic, creative but tasteful card, colour used, front and back. I have attached a sample card that I liked very much from another individual to give you an idea of the theme/approach, but not colour. Ideally the graphic elements of the Brightwell Logo are brought into the design.

Target Market(s)

North America

Industry/Entity Type

Film Production

Contact Information for Business Card

Mirela Vantasch
President/Founder
Brightwell Pictures Inc.
587 914 3362
mirela@brightwellpix.tv

Font styles to use
Sans Serif

Colors
6b449b
5c5c5c
fdfdfd
000000

Requirements
Must have
• Logo, name, Company name, email and cell number. no Address line to be included.
Should not have
• any unrelated GFX elements, serif fonts

```html
<!DOCTYPE html>
<html lang="en">
<head>
<meta charset="utf-8">
<title>Brightwell Pictures – Business Card</title>
<link rel="stylesheet" href="https://fonts.googleapis.com/css2?family=Roboto:wght@400;700&family=Roboto+Condensed:wght@700&display=swap">
<style>
  :root {
    --purple: #5b2a8a;
    --purple-soft: #ebe6ef;
    --grey: #5c5c5c;
    --paper: #fdfdfd;
    --backdrop: #2b2b2b;
    --white: #ffffff;
  }
  * { margin: 0; padding: 0; box-sizing: border-box; }
  html, body { width: 1200px; height: 960px; overflow: hidden; }
  body {
    background: var(--backdrop);
    position: relative;
    font-family: "Roboto", Arial, sans-serif;
  }
  .card {
    position: absolute;
    width: 600px;
    height: 343px;
    overflow: hidden;
    box-shadow: 0 3px 6px rgba(0,0,0,.45);
  }
  .card--front { left: 314px; top: 113px; background: var(--paper); }
  .card--back  { left: 311px; top: 472px; background: var(--purple); }

  .front__ring {
    position: absolute;
    left: 267px; top: 37px;
    width: 340px; height: 340px;
  }
  .wordmark {
    font-family: "Roboto", Arial, sans-serif;
    font-weight: 700;
    line-height: 1;
  }
  .wordmark__name { display: block; font-size: 52px; letter-spacing: -1.5px; }
  .wordmark__sub  { display: block; font-size: 12px; letter-spacing: 9px; margin-top: 4px; }

  .front__logo {
    position: absolute; left: 56px; top: 60px;
    color: var(--purple);
  }
  .front__logo .wordmark__sub { text-align: right; margin-right: -9px; }

  .contact {
    position: absolute; left: 57px; top: 233px;
    list-style: none;
    font-size: 14.5px; color: #444;
  }
  .contact li { display: flex; align-items: center; height: 19px; }
  .contact svg { width: 13px; height: 13px; margin-right: 8px; fill: var(--purple); }

  .person {
    position: absolute; right: 54px; top: 239px;
    text-align: right;
    font-family: "Roboto Condensed", "Arial Narrow", sans-serif;
    font-weight: 700;
  }
  .person__name { font-size: 22px; color: var(--purple); line-height: 1.1; }
  .person__role { font-size: 16px; color: var(--grey); line-height: 1.2; }

  .back__logo {
    position: absolute; left: 0; right: 0; top: 126px;
    text-align: center; color: var(--white);
  }
  .back__logo .wordmark__name { font-size: 58px; }
  .back__logo .wordmark__sub  { font-size: 13px; letter-spacing: 10px; margin-top: 6px; }

  .back__web {
    position: absolute; left: 0; right: 0; top: 281px;
    text-align: center; color: var(--white);
    font-size: 15px; letter-spacing: 5px;
  }
</style>
</head>
<body>

<section class="card card--front">
  <svg class="front__ring" viewBox="0 0 340 340" aria-hidden="true">
    <circle cx="170" cy="170" r="140" fill="none" stroke="var(--purple-soft)" stroke-width="58"/>
  </svg>

  <div class="front__logo wordmark">
    <span class="wordmark__name">Brightwell</span>
    <span class="wordmark__sub">PICTURES</span>
  </div>

  <ul class="contact">
    <li>
      <svg viewBox="0 0 24 24"><path d="M6.6 10.8a15.1 15.1 0 0 0 6.6 6.6l2.2-2.2c.3-.3.7-.4 1-.2 1.1.4 2.3.6 3.6.6.6 0 1 .4 1 1V20c0 .6-.4 1-1 1C10.6 21 3 13.4 3 4c0-.6.4-1 1-1h3.5c.6 0 1 .4 1 1 0 1.3.2 2.5.6 3.6.1.3 0 .7-.2 1z"/></svg>
      587 914 3362
    </li>
    <li>
      <svg viewBox="0 0 24 24"><path d="M2 5h20v14H2zm2 2v.5l8 5 8-5V7zm0 2.8V17h16V9.8l-8 5z"/></svg>
      mirela@brightwellpix.tv
    </li>
    <li>
      <svg viewBox="0 0 24 24"><path d="M12 2a10 10 0 1 0 0 20 10 10 0 0 0 0-20zm-1 17.9A8 8 0 0 1 4.2 10.8L9 15.6v1a2 2 0 0 0 2 2zm6.9-2.5a2 2 0 0 0-1.9-1.4h-1v-3a1 1 0 0 0-1-1H8v-2h2a1 1 0 0 0 1-1V7h2a2 2 0 0 0 2-2v-.4a8 8 0 0 1 2.9 12.8z"/></svg>
      brightwellpix.tv
    </li>
  </ul>

  <div class="person">
    <p class="person__name">Mirela Vantasch</p>
    <p class="person__role">Director/ Producer</p>
  </div>
</section>

<section class="card card--back">
  <div class="back__logo wordmark">
    <span class="wordmark__name">Brightwell</span>
    <span class="wordmark__sub">PICTURES</span>
  </div>
  <p class="back__web">www.brightwellpix.tv</p>
</section>

</body>
</html>
```